Luxurious , elegant , fancy styling flat iron box

I need a flat iron box design for my new product . I’m interested in something fancy, elegant and sophisticated.
the name of the product is

Velvet Crest

Elite World Class Performance
Nano Titanium Professional Flat Iron
Heats up to 470 degrees
Rated #1
Extention and Natural Hair Straighter for thick and course hair

Target Market(s)

Women

Industry/Entity Type

Hair And Beauty

Font styles to use
Script

Colors
1b1b1b
757575
5c5c5c

Requirements
Must have
• Fancy yet understandable writing
Should not have
• Too many colors , block writing

```html
<!DOCTYPE html>
<html lang="en">
<head>
<meta charset="utf-8">
<title>Velvet Crest – Flat Iron Box</title>
<link rel="stylesheet" href="https://fonts.googleapis.com/css2?family=Roboto:wght@300;400;700&display=swap">
<style>
  :root {
    --page: #eeeeee;
    --box-black: #1b1b1b;
    --box-deep: #0f0f0f;
    --facet-mid: #5c5c5c;
    --divider: #757575;
    --ink-light: #e6e6e6;
    --ink-soft: #bdbdbd;
    --ink-dim: #8a8a8a;
  }
  * { margin: 0; padding: 0; box-sizing: border-box; }
  html, body { width: 1200px; height: 800px; overflow: hidden; }
  body {
    background: var(--page);
    font-family: "Roboto", Arial, sans-serif;
    display: flex;
    flex-direction: column;
    align-items: center;
    justify-content: center;
    gap: 36px;
  }
  .box-panel {
    width: 1040px;
    background: radial-gradient(ellipse at 35% 40%, #2a2a2a 0%, var(--box-black) 55%, var(--box-deep) 100%);
    display: flex;
    position: relative;
    box-shadow: 0 10px 30px rgba(0,0,0,0.18);
  }
  .panel-top { height: 300px; }
  .panel-front { height: 230px; }
  .brand-area {
    flex: 0 0 640px;
    position: relative;
    display: flex;
    align-items: center;
    padding-left: 70px;
  }
  .facet-band {
    position: absolute;
    left: 0;
    top: 50%;
    transform: translateY(-50%);
    width: 560px;
    height: 120px;
    background: linear-gradient(90deg, rgba(92,92,92,0.55) 0%, rgba(92,92,92,0.35) 45%, rgba(27,27,27,0) 100%);
  }
  .panel-front .facet-band { height: 100px; }
  .brand-name {
    position: relative;
    font-family: "Roboto", Arial, sans-serif;
    font-weight: 400;
    font-size: 56px;
    color: var(--ink-light);
    line-height: 1;
  }
  .panel-front .brand-name { font-size: 50px; }
  .panel-divider {
    width: 3px;
    background: var(--divider);
    opacity: 0.7;
  }
  .product-area {
    flex: 1;
    padding: 0 50px;
    display: flex;
    flex-direction: column;
    justify-content: center;
  }
  .product-title {
    font-weight: 300;
    font-size: 30px;
    line-height: 1.35;
    color: var(--ink-light);
  }
  .product-claim {
    margin-top: 14px;
    font-size: 15px;
    font-weight: 400;
    color: var(--ink-soft);
  }
  .product-details { color: var(--ink-soft); font-size: 14px; }
  .product-use { line-height: 1.45; }
  .product-rule {
    border: 0;
    border-top: 1px solid var(--divider);
    margin: 10px 0;
  }
  .product-specs { display: flex; justify-content: space-between; gap: 16px; }
  .product-specs strong { color: var(--ink-light); font-weight: 700; }
  .product-rank { color: var(--ink-dim); white-space: nowrap; }
</style>
</head>
<body>
  <section class="box-panel panel-top">
    <div class="brand-area">
      <div class="facet-band" role="img" aria-label="Faceted diamond-cut triangle pattern in dark greys"></div>
      <div class="brand-name">Velvet Crest</div>
    </div>
    <div class="panel-divider"></div>
    <div class="product-area">
      <p class="product-title">Nano Titanium<br>Professional Flat Iron</p>
      <p class="product-claim">Elite World Class Performance</p>
    </div>
  </section>

  <section class="box-panel panel-front">
    <div class="brand-area">
      <div class="facet-band" role="img" aria-label="Faceted diamond-cut triangle pattern in dark greys"></div>
      <div class="brand-name">Velvet Crest</div>
    </div>
    <div class="panel-divider"></div>
    <div class="product-area product-details">
      <div class="product-specs">
        <p class="product-use">Extention and Natural Hair Straighter<br>for thick and course hair</p>
        <p class="product-rank">Rated #1</p>
      </div>
      <hr class="product-rule">
      <p>Heats up to <strong>470</strong> degrees</p>
    </div>
  </section>
</body>
</html>
```